新しくオープンしたラーメン居酒屋の新メニューのチラシ制作をお願いします。
こだわりが強く、比較的高級なラーメン屋です。高級感のある本格的なデザイン、訴求力がありながらも上品なデザインを希望します。
サイズ:A4サイズ
ノビテルで入稿します。
編集できるイラストレーターとPDFファイルでの納品をお願いします。

イメージ通りでした。

この度はたくさんのご応募ありがとうございます。今後ともよろしくお願いいたします。

```html
<!DOCTYPE html>
<html lang="ja">
<head>
<meta charset="utf-8">
<title>冷製 鯛出汁塩山椒そば</title>
<link rel="stylesheet" href="https://fonts.googleapis.com/css2?family=Shippori+Mincho+B1:wght@500;700;800&display=swap">
<style>
  :root {
    --ink: #0b0b0b;
    --charcoal: #1c1c1c;
    --white: #ffffff;
    --gold-deep: #8a4a08;
    --gold: #d98a1c;
    --gold-light: #f3c15a;
    --broth: #f6d27a;
  }
  * { margin: 0; padding: 0; box-sizing: border-box; }
  html, body { width: 846px; height: 1200px; overflow: hidden; background: var(--ink); }
  .flyer {
    position: relative;
    width: 846px;
    height: 1200px;
    overflow: hidden;
    background: linear-gradient(180deg, var(--charcoal) 0%, var(--ink) 30%);
    font-family: "Shippori Mincho B1", serif;
    color: var(--white);
  }
  .dish-photo {
    position: absolute;
    left: -60px;
    top: 210px;
    width: 920px;
    height: 1040px;
    background:
      radial-gradient(ellipse 44% 40% at 46% 58%, var(--broth) 0%, var(--gold-light) 35%, var(--gold) 68%, var(--gold-deep) 88%, transparent 100%),
      radial-gradient(ellipse 70% 55% at 50% 60%, rgba(120,60,10,.6) 0%, transparent 75%);
  }
  .season-badge {
    position: absolute;
    left: 28px;
    top: 16px;
    width: 62px;
    height: 196px;
    border: 2px solid var(--white);
    display: flex;
    align-items: center;
    justify-content: center;
    writing-mode: vertical-rl;
    font-size: 40px;
    font-weight: 700;
    letter-spacing: 2px;
  }
  .title-block { position: absolute; left: 106px; top: 18px; }
  .title-block .style-tag { font-size: 42px; font-weight: 700; line-height: 1; }
  .title-block .dish-name {
    margin-top: 10px;
    font-size: 76px;
    font-weight: 800;
    line-height: 1;
    letter-spacing: 1px;
  }
  .title-block .price {
    margin-top: 14px;
    font-size: 58px;
    font-weight: 700;
    line-height: 1;
  }
  .description {
    position: absolute;
    right: 22px;
    top: 258px;
    writing-mode: vertical-rl;
    font-size: 25px;
    font-weight: 700;
    line-height: 40px;
    letter-spacing: 1px;
    text-shadow: 0 0 6px rgba(70,30,0,.85), 0 0 2px rgba(70,30,0,.9);
  }
  .no-additives {
    position: absolute;
    right: 38px;
    bottom: 22px;
    font-size: 19px;
    font-weight: 700;
    text-shadow: 0 0 4px rgba(0,0,0,.8);
  }
</style>
</head>
<body>
  <main class="flyer">
    <div class="dish-photo" role="img" aria-label="冷製鯛出汁塩山椒そばの写真。金色の器に澄んだスープ、細麺、海老、ミニトマト、青菜、豆腐、海苔"></div>

    <div class="season-badge">夏季限定</div>

    <header class="title-block">
      <p class="style-tag">冷製</p>
      <h1 class="dish-name">鯛出汁塩山椒そば</h1>
      <p class="price">¥1,000</p>
    </header>

    <p class="description">濃密ながら清らかな<br>真鯛出汁、香りの異なる２種類の山椒を<br>漬け込んだ香味油、自家製の塩だれが<br>三位一体となった一杯。</p>

    <p class="no-additives">化学調味料不使用</p>
  </main>
</body>
</html>
```